Stationary For Harbor Allies
Harbor Allies
Project: Stationary For Harbor Allies
Stationary For Harbor Allies - Consulting
Creative Brief
Professional
Lou Brannick
President
547 Marlow Ln Spring Branch, TX 78070
lbrannick@harborallies4.com
www.harborallies4.com
I will need letterhead and envelopes as well as business cards. Feel free to try different fonts.
quelnor42 quelnor42
Designers, Please focus more on the letterhead and envelopes than the business cards. Thanks!

```html
<!DOCTYPE html>
<html lang="en">
<head>
<meta charset="utf-8">
<title>Harbor Allies – Business Card</title>
<link rel="stylesheet" href="https://fonts.googleapis.com/css2?family=Open+Sans:wght@400;600;700&display=swap">
<style>
  :root {
    --stage: #cfd0d2;
    --card: #ffffff;
    --brand-blue: #2a5ea8;
    --ink-grey: #6d6f73;
    --soft-grey: #9a9c9f;
  }
  * { margin: 0; padding: 0; box-sizing: border-box; }
  html, body {
    width: 1200px; height: 902px; overflow: hidden;
    background: var(--stage);
    font-family: "Open Sans", Arial, sans-serif;
  }
  .stage {
    width: 1200px; height: 902px;
    display: flex; flex-direction: column;
    align-items: center; justify-content: center; gap: 44px;
  }
  .card {
    position: relative;
    width: 640px; height: 366px;
    background: var(--card);
    box-shadow: 0 6px 18px rgba(0,0,0,0.18);
  }
  /* Back of card */
  .contact-block {
    position: absolute; right: 48px; top: 120px;
    text-align: right; font-size: 13px; line-height: 22px;
    color: var(--ink-grey);
  }
  .contact-line { display: flex; justify-content: flex-end; align-items: center; gap: 7px; }
  .contact-line svg { width: 11px; height: 11px; fill: var(--brand-blue); }
  .website {
    position: absolute; left: 48px; bottom: 40px;
    font-size: 16px; color: var(--soft-grey); letter-spacing: 1px;
  }
  .website strong { color: var(--brand-blue); font-weight: 700; }
  /* Front of card */
  .brand-name {
    position: absolute; left: 56px; bottom: 64px;
    display: flex; align-items: center; gap: 14px;
  }
  .brand-mark {
    width: 46px; height: 46px; border-radius: 50%;
    background: var(--brand-blue);
  }
  .brand-text {
    font-size: 34px; font-weight: 400; color: var(--brand-blue);
    letter-spacing: 0.5px;
  }
  .person {
    position: absolute; right: 52px; top: 128px; text-align: right;
  }
  .person-name { font-size: 19px; font-weight: 700; color: var(--brand-blue); }
  .person-title { font-size: 15px; color: var(--ink-grey); margin-top: 2px; }
</style>
</head>
<body>
<main class="stage">
  <section class="card card-back">
    <div class="contact-block">
      <p>547 Marlow Ln</p>
      <p>Spring Branch, TX 78070</p>
      <p class="contact-line">512.555.0148
        <svg viewBox="0 0 24 24" aria-hidden="true"><path d="M6.6 10.8a15 15 0 0 0 6.6 6.6l2.2-2.2a1 1 0 0 1 1-.25 11.4 11.4 0 0 0 3.6.6 1 1 0 0 1 1 1V20a1 1 0 0 1-1 1A17 17 0 0 1 3 4a1 1 0 0 1 1-1h3.5a1 1 0 0 1 1 1c0 1.25.2 2.45.6 3.6a1 1 0 0 1-.25 1z"/></svg>
      </p>
      <p class="contact-line">mara@harborallies4.com
        <svg viewBox="0 0 24 24" aria-hidden="true"><path d="M2 5h20v14H2z"/></svg>
      </p>
    </div>
    <p class="website">www.<strong>harborallies4</strong>.com</p>
  </section>

  <section class="card card-front">
    <div class="brand-name">
      <span class="brand-mark"></span>
      <span class="brand-text">Harbor Allies</span>
    </div>
    <div class="person">
      <p class="person-name">Mara Ellison</p>
      <p class="person-title">Owner</p>
    </div>
  </section>
</main>
</body>
</html>
```